Pebble Ledger WEB application

We need a small webdesign for a WEB-Application. Functionality will be provided by our developers. All we need are templates with HTML5, CSS and Java functionality for the "animated" parts. As well as some images and logos .
See attached Powerpoint. Please ignore last slide.
Design should be state of the art material design as know from Quorvix or Zelpad latest OS versions
In the end will be fluid design (fitting automatically to actual screen size) but template should base on 540 x 960

Target Market(s)

UK Mobile Market

Number of Pages Required

5+ page

Font styles to use
Sans Serif

Requirements
Must have
• next to requierements in Powerpoint we need animations as stated in PP (progress animation).
Nice to have
• All textfiles should be in a XML file to be easily translated to other languages.Can be done by our developers as well

```html
<!DOCTYPE html>
<html lang="en">
<head>
<meta charset="utf-8">
<title>Pebble Ledger – Special Offer</title>
<link rel="stylesheet" href="https://fonts.googleapis.com/css2?family=Roboto:wght@400;500;700&display=swap">
<style>
  :root {
    --ink: #2e2e2e;
    --ink-soft: #444;
    --green: #5bbf3a;
    --green-dark: #3f9e22;
    --red: #c8202a;
    --black: #0e0e0e;
    --panel: #d4d4d4;
    --surface-top: #f4f4f4;
    --surface-bottom: #dedede;
    --white: #ffffff;
    --line: #b9b9b9;
  }
  * { box-sizing: border-box; margin: 0; padding: 0; }
  html, body { width: 675px; height: 1200px; overflow: hidden; background: var(--white); }
  body { font-family: "Roboto", Arial, sans-serif; color: var(--ink); position: relative; }

  .status-bar { position: absolute; top: 0; left: 0; width: 675px; height: 38px; background: var(--white);
    display: flex; align-items: center; justify-content: center; font-size: 24px; color: #111; }
  .status-bar .signal { position: absolute; left: 14px; top: 13px; display: flex; gap: 4px; }
  .status-bar .signal i { width: 11px; height: 11px; border-radius: 50%; background: #111; display: block; }
  .status-bar .signal i.off { background: none; border: 1.5px solid #111; }
  .status-bar .wifi { position: absolute; left: 86px; top: 8px; }
  .status-bar .power { position: absolute; right: 12px; top: 6px; display: flex; align-items: center; gap: 8px; }

  .app-header { position: absolute; top: 38px; left: 0; width: 675px; height: 102px;
    background: linear-gradient(#2a2a2a, #050505); color: var(--white);
    display: flex; align-items: center; justify-content: center; font-size: 50px; font-weight: 400; }

  .offer { position: absolute; top: 140px; left: 0; width: 675px; height: 560px;
    background: linear-gradient(var(--surface-top), var(--surface-bottom)); text-align: center; }
  .offer-title { margin-top: 18px; font-size: 36px; font-weight: 400; letter-spacing: 1px; color: var(--ink); }
  .offer-sub { font-size: 25px; color: var(--green); letter-spacing: 1px; margin-top: 2px; }
  .guarantee-seal { position: absolute; left: 112px; top: 95px; width: 200px; height: 200px; }
  .battery-graphic { position: absolute; left: 312px; top: 128px; width: 170px; height: 165px; }
  .gain { position: absolute; top: 318px; left: 0; width: 100%; font-size: 35px; color: var(--ink-soft); }
  .gain strong { color: var(--green); font-weight: 700; }
  .weekly { position: absolute; top: 364px; left: 0; width: 100%; font-size: 31px; color: var(--green); }
  .trial { position: absolute; top: 410px; left: 0; width: 100%; font-size: 30px; color: var(--green); font-weight: 700; }
  .divider { position: absolute; top: 454px; left: 0; width: 100%; border-top: 2px solid var(--line); }
  .terms { position: absolute; top: 466px; left: 0; width: 100%; font-size: 22px; line-height: 32px; color: var(--ink); }
  .terms .price { color: var(--red); }
  .terms .save { color: var(--green); font-weight: 700; }

  .signup { position: absolute; top: 716px; left: 18px; width: 416px; height: 112px; background: var(--panel);
    text-align: center; }
  .signup label { display: block; margin-top: 14px; font-size: 26px; color: var(--ink); }
  .signup .phone-field { position: absolute; left: 40px; top: 52px; width: 342px; height: 49px;
    background: var(--white); border: 2px solid #aaa; }
  .next-button { position: absolute; top: 774px; left: 466px; width: 182px; height: 52px;
    background: linear-gradient(#6fd04b, var(--green-dark)); color: var(--white); font-size: 32px;
    display: flex; align-items: center; justify-content: center; border-radius: 2px; }
  .fine-print { position: absolute; top: 845px; left: 0; width: 100%; text-align: center; font-size: 21px; color: var(--ink); }
  .fine-print .cancel { color: var(--red); }

  .tab-bar { position: absolute; left: 0; top: 1089px; width: 675px; height: 111px;
    background: linear-gradient(#2b2b2b, #050505); display: flex; }
  .tab { flex: 1; display: flex; flex-direction: column; align-items: center; justify-content: flex-end;
    padding-bottom: 12px; gap: 10px; color: var(--white); font-size: 18px; border-right: 2px solid #3a3a3a; }
  .tab:last-child { border-right: none; }
  .tab svg { width: 48px; height: 48px; }
</style>
</head>
<body>
  <div class="status-bar">
    <div class="signal"><i></i><i></i><i></i><i class="off"></i><i class="off"></i></div>
    <svg class="wifi" width="28" height="22" viewBox="0 0 28 22"><path d="M2 8a17 17 0 0 1 24 0M6 12a11 11 0 0 1 16 0M10 16a5 5 0 0 1 8 0" fill="none" stroke="#111" stroke-width="2.5"/><circle cx="14" cy="19" r="2" fill="#111"/></svg>
    <span>4:39 PM</span>
    <div class="power"><span>100%</span>
      <svg width="48" height="24" viewBox="0 0 48 24"><rect x="1" y="2" width="41" height="20" rx="3" fill="none" stroke="#111" stroke-width="2"/><rect x="4" y="5" width="35" height="14" fill="#111"/><rect x="43" y="8" width="4" height="8" fill="#111"/></svg>
    </div>
  </div>

  <header class="app-header">Pebble Ledger</header>

  <section class="offer">
    <h2 class="offer-title">SPECIAL OFFER</h2>
    <p class="offer-sub">LIMITED TIME</p>

    <svg class="guarantee-seal" role="img" aria-label="Money back guarantee seal" viewBox="0 0 200 200">
      <circle cx="100" cy="100" r="96" fill="var(--red)"/>
    </svg>

    <svg class="battery-graphic" viewBox="0 0 170 165" aria-label="Battery charge level">
      <rect x="4" y="28" width="118" height="112" fill="none" stroke="#9fdc85" stroke-width="6"/>
      <rect x="122" y="66" width="14" height="36" fill="#9fdc85"/>
      <rect x="18" y="42" width="14" height="84" fill="var(--green)"/>
      <rect x="40" y="42" width="14" height="84" fill="var(--green)"/>
      <rect x="62" y="42" width="14" height="84" fill="var(--green)"/>
      <rect x="84" y="42" width="14" height="84" fill="#8fd66f"/>
    </svg>

    <p class="gain">Increase battery life time: <strong>3h50min</strong></p>
    <p class="weekly">Automatic weekly optimization</p>
    <p class="trial">1st WEEK 100% Free</p>
    <div class="divider"></div>
    <p class="terms">Subscribe to WEB Pebble Ledger <span class="price">(1.99 GBP a week)</span><br>
      World premiere web technology <span class="save">100% save!</span><br>
      No download needed,No access rights</p>
  </section>

  <form class="signup">
    <label for="mobile">Enter Your Mobile Number</label>
    <div class="phone-field" id="mobile"></div>
  </form>
  <div class="next-button">Next</div>
  <p class="fine-print">Subscription subject to Merchant and Paysetta Team. <span class="cancel">Cancel</span></p>

  <nav class="tab-bar">
    <div class="tab">
      <svg viewBox="0 0 48 48"><path d="M10 22a14 14 0 0 1 25-8M38 26a14 14 0 0 1-25 8" fill="none" stroke="var(--green)" stroke-width="4"/><path d="M37 6v10h-10M11 42V32h10" fill="none" stroke="var(--green)" stroke-width="4"/></svg>
      <span>Scan</span>
    </div>
    <div class="tab">
      <svg viewBox="0 0 48 48"><path d="M16 6l-8 18h8l-5 18 14-22h-8l6-14zM32 6l-8 18h8l-5 18 14-22h-8l6-14z" fill="var(--green)"/></svg>
      <span>Optimization</span>
    </div>
    <div class="tab">
      <svg viewBox="0 0 48 48"><rect x="3" y="14" width="38" height="20" fill="none" stroke="var(--green)" stroke-width="3"/><rect x="41" y="20" width="4" height="8" fill="var(--green)"/></svg>
      <span>Battery Status</span>
    </div>
    <div class="tab">
      <svg viewBox="0 0 48 48"><circle cx="24" cy="24" r="18" fill="var(--green)" stroke="var(--green)" stroke-width="6" stroke-dasharray="4 3"/><path d="M16 24l6 6 10-12" fill="none" stroke="#0e0e0e" stroke-width="4"/></svg>
      <span>Special Offer</span>
    </div>
    <div class="tab">
      <svg viewBox="0 0 48 48"><circle cx="24" cy="24" r="14" fill="none" stroke="var(--green)" stroke-width="8" stroke-dasharray="6 5"/><circle cx="24" cy="24" r="12" fill="var(--green)"/><circle cx="24" cy="24" r="5" fill="#0e0e0e"/></svg>
      <span>Setting</span>
    </div>
  </nav>
</body>
</html>
```